Quorvia medical teaching of the future

responsive website, onepager, for medical technology company. It has to look clean and high tech.

Look & feel
• Responsive
• Clean
• Combination icons + foto's
• Integration of a YouTube video

Landingpage items

• Header: picture + 'a video-based teaching platform for surgical procedures'
• About Deferred live medical teaching: Short description
• Features
o Video
o Teaching platform

• Benefits:
o More effective learning
o Faster sharing of knowledge & tecniques
o More cost effective

• References

• Products:
o Live (+link to more info)
o bTamo (+ link to more info)
o bTamo local (+link to more info)
o bTamo cloud (+ link to more info)

• Solutions:
o For medical device companies (+link to more info)
o Doctor and surgeons (+link to more info)
o Medical conferences (+link to more info)

Target Market(s)

medical device companies
surgeons and doctors
conference organisers

Industry/Entity Type

It Company

Number of Pages Required

1 page

Requirements
Must have
• Landingpage items
• • Header: picture + 'a video-based teaching platform for surgical procedures'
• • About Deferred live medical teaching: Short description
• • Features
• o Video
• o Teaching platform
• • Benefits:
• o More effective learning
• o Faster sharing of knowledge & tecniques
• o More cost effective
• • References
• • Products:
• o Live (+link to more info)
• o bTamo (+ link to more info)
• o bTamo local (+link to more info)
• o bTamo cloud (+ link to more info)
• • Solutions:
• o For medical device companies (+link to more info)
• o Doctor and surgeons (+link to more info)
• o Medical conferences (+link to more info)
Nice to have
• possibilty to show video

```html
<!DOCTYPE html>
<html lang="en">
<head>
<meta charset="utf-8">
<title>Quorvia – Medical teaching of the future</title>
<link href="https://fonts.googleapis.com/css2?family=Montserrat:wght@400;500;600;700&family=Open+Sans:wght@400;600;700&display=swap" rel="stylesheet">
<style>
:root{
  --teal:#22a394;
  --teal-light:#2bb5a5;
  --teal-dark:#1b8c80;
  --red:#f0454a;
  --ink:#2b2b2b;
  --body:#6b6b6b;
  --grey-band:#ececec;
  --grey-btn:#d6d6d6;
  --topbar:#eeeeee;
  --white:#ffffff;
}
*{margin:0;padding:0;box-sizing:border-box}
html,body{width:1200px;height:3327px;overflow:hidden}
body{font-family:"Open Sans",Arial,sans-serif;color:var(--body);background:var(--white);position:relative}
h1,h2,h3,.brand,.nav a,.btn{font-family:"Montserrat",Arial,sans-serif}

/* top bar */
.topbar{position:absolute;top:0;left:0;width:1200px;height:35px;background:var(--topbar)}
.topbar .social{position:absolute;left:860px;top:12px;display:flex;gap:16px}
.topbar .social span{width:10px;height:10px;border-radius:50%;background:#9a9a9a;display:block}
.login{position:absolute;left:962px;top:0;width:158px;height:35px;background:var(--teal);color:var(--white);font:600 13px "Open Sans",sans-serif;display:flex;align-items:center;justify-content:center;gap:8px}

/* header */
.header{position:absolute;top:35px;left:0;width:1200px;height:131px;background:var(--white)}
.brand{position:absolute;left:67px;top:36px;display:flex;align-items:center;gap:14px;font-weight:600;font-size:44px;color:var(--teal);letter-spacing:-0.5px}
.brand .dot{width:44px;height:44px;border-radius:50%;background:var(--teal)}
.contact{position:absolute;top:52px;display:flex;gap:10px;align-items:center;font-size:13px;color:#333;line-height:1.4}
.contact b{font-weight:700;font-size:14px;display:block}
.contact small{font-size:12px;color:#555}
.contact.phone{left:738px}
.contact.hours{left:966px}

/* hero */
.hero{position:absolute;top:166px;left:0;width:1200px;height:595px;background:linear-gradient(135deg,#6f8c8a 0%,#9fb4b1 35%,#4f6d6e 70%,#36504f 100%)}
.nav{position:absolute;top:0;left:67px;width:1053px;height:54px;background:var(--teal);display:flex}
.nav a{color:var(--white);font-size:13px;font-weight:500;text-decoration:none;display:flex;align-items:center;padding:0 24px;letter-spacing:.3px}
.nav a.active{background:var(--red)}
.search{position:absolute;top:0;left:1067px;width:53px;height:54px;background:#3f9c92;display:flex;align-items:center;justify-content:center}
.hero h1{position:absolute;top:186px;left:0;width:1200px;text-align:center;color:var(--white);font-size:40px;font-weight:600;line-height:1.35;text-shadow:0 2px 6px rgba(0,0,0,.35)}
.play{position:absolute;border-radius:50%;background:var(--red);display:flex;align-items:center;justify-content:center}
.hero .play{left:550px;top:312px;width:100px;height:100px}

/* about */
.about{position:absolute;top:761px;left:0;width:1200px;height:570px}
.about .photo{position:absolute;left:100px;top:93px;width:360px;height:362px;background:linear-gradient(160deg,#c9cfd3 0%,#7d8f93 45%,#3e5a5e 100%)}
.about .text{position:absolute;left:515px;top:82px;width:560px}
.about h2{font-size:40px;font-weight:600;color:var(--ink);margin-bottom:22px}
.about p{font-size:14.5px;line-height:1.65;margin-bottom:18px}
.about p strong{color:#333;font-weight:600;display:block}

/* benefits */
.benefits{position:absolute;top:1331px;left:0;width:1200px;height:437px;background:var(--grey-band)}
.benefits .panel{position:absolute;left:0;top:0;width:388px;height:437px;background:var(--teal)}
.benefits h2{position:absolute;left:67px;top:50px;color:var(--white);font-size:34px;font-weight:500}
.benefits .sub{position:absolute;left:67px;top:104px;width:280px;color:var(--white);font-size:12.5px;line-height:1.55}
.tab{position:absolute;left:67px;width:321px;height:44px;background:var(--teal-light);color:var(--white);font:500 14px "Montserrat",sans-serif;display:flex;align-items:center;padding-left:20px;text-transform:uppercase}
.tab.active{background:var(--red)}
.video{position:absolute;left:492px;top:46px;width:559px;height:344px;background:var(--white);padding:8px}
.video .frame{width:100%;height:100%;background:linear-gradient(120deg,#7aa29c 0%,#4d7774 40%,#8bb0aa 70%,#3d5e5c 100%);position:relative}
.video .play{left:236px;top:122px;width:84px;height:84px}

/* products */
.products{position:absolute;top:1768px;left:0;width:1200px;height:610px}
.section-title{position:absolute;left:0;width:1200px;text-align:center;font-size:40px;font-weight:600;color:var(--ink)}
.products .section-title{top:56px}
.product-row{position:absolute;left:56px;top:158px;width:1088px;display:flex}
.product{width:272px;text-align:center;border-right:1px solid #e8e8e8;padding:0 12px;height:292px}
.product:last-child{border-right:none}
.product .shot{width:200px;height:144px;margin:18px auto 0;background:linear-gradient(160deg,#9a9a8a 0%,#4a4f48 55%,#222 100%);border-radius:4px}
.product h3{font-size:24px;font-weight:500;color:var(--ink);margin-top:14px}
.product p{font-size:13px;line-height:1.6;margin-top:6px}
.more{display:inline-block;color:var(--red);font-size:13px;margin-top:6px;text-decoration:none}

/* solutions */
.solutions{position:absolute;top:2378px;left:0;width:1200px;height:650px;background:var(--grey-band)}
.solutions .section-title{top:46px}
.card{position:absolute;top:150px;width:328px;height:422px;background:var(--white)}
.card .img{height:173px}
.card h3{font-size:20px;font-weight:600;color:var(--ink);margin:24px 12px 10px}
.card p{font-size:13.5px;line-height:1.65;margin:0 12px}
.card .btn{position:absolute;left:12px;bottom:8px;width:304px;height:48px;background:var(--grey-btn);color:#444;font-size:15px;font-weight:600;display:flex;align-items:center;justify-content:center;text-decoration:none}
.card .btn.hot{background:var(--red);color:var(--white)}

/* footer */
.footer{position:absolute;top:3028px;left:0;width:1200px;height:299px;background:var(--teal);text-align:center;color:var(--white)}
.footer .brand{position:static;display:inline-flex;margin-top:62px;color:var(--white)}
.footer .brand .dot{background:var(--white)}
.footer .links{margin-top:34px;font:500 12.5px "Montserrat",sans-serif}
.footer .links a{color:var(--white);text-decoration:none;padding:0 9px}
.footer .links i{font-style:normal;opacity:.8}
.footer .copy{margin-top:18px;font-size:13px}
.footer .diamonds{display:flex;justify-content:center;gap:18px;margin-top:22px}
.footer .diamonds span{width:28px;height:28px;background:#1d3f3b;transform:rotate(45deg);display:block}
</style>
</head>
<body>

<div class="topbar">
  <div class="social"><span></span><span></span><span></span></div>
  <div class="login">
    <svg width="12" height="12" viewBox="0 0 12 12"><circle cx="6" cy="4" r="2.6" fill="#fff"/><path d="M1 12c0-3 2.2-4.6 5-4.6S11 9 11 12z" fill="#fff"/></svg>
    Distributor Login
  </div>
</div>

<header class="header">
  <div class="brand"><span class="dot"></span>Quorvia</div>
  <div class="contact phone">
    <svg width="24" height="24" viewBox="0 0 24 24"><path d="M6 3l3 4-2 2c1 3 4 6 7 7l2-2 4 3-2 3C11 20 4 13 3 5z" fill="none" stroke="#22a394" stroke-width="1.6"/></svg>
    <div><b>1.800.555.0142</b><small>info@quorvia-teach.com</small></div>
  </div>
  <div class="contact hours">
    <svg width="24" height="24" viewBox="0 0 24 24"><circle cx="12" cy="12" r="9.5" fill="none" stroke="#22a394" stroke-width="1.6"/><path d="M12 6v6l4 3" fill="none" stroke="#22a394" stroke-width="1.6"/></svg>
    <div><b>7:30 AM - 7:30 PM</b><small>Monday to Saturday</small></div>
  </div>
</header>

<section class="hero" role="img" aria-label="Surgical team in scrubs performing an operation in a modern operating room">
  <nav class="nav">
    <a class="active" href="#">HOME</a><a href="#">ABOUT US</a><a href="#">FEATURES</a><a href="#">BENEFITS</a><a href="#">REFERENCES</a><a href="#">PRODUCTS</a><a href="#">SOLUTIONS</a><a href="#">CONTACT</a>
  </nav>
  <div class="search"><svg width="22" height="22" viewBox="0 0 22 22"><circle cx="9" cy="9" r="6.5" fill="none" stroke="#fff" stroke-width="2.4"/><path d="M14 14l6 6" stroke="#fff" stroke-width="2.6"/></svg></div>
  <h1>Quorvia changes the way medical<br>procedures are taught</h1>
  <div class="play"><svg width="36" height="40" viewBox="0 0 36 40"><path d="M6 2l28 18L6 38z" fill="#fff"/></svg></div>
</section>

<section class="about">
  <div class="photo" role="img" aria-label="Operating theatre with surgical lights and monitors showing endoscopic video"></div>
  <div class="text">
    <h2>About Quorvia</h2>
    <p>Almost daily medical device companies, doctors and surgeons all over the world develop new or breakthrough products, medical and surgical techniques. These techniques save lives or increase the survival rate of some patients.</p>
    <p>It is therefore very important that these medical device companies, doctors and surgeons share their knowledge as fast and accurate as possible. The current methods to share this knowledge are peer-to-peer live medical teachings and live medical teaching at conferences.</p>
    <p><strong>Peer-to-peer live medical teaching</strong>Healthcare companies contract top surgeons to do teaching sessions with their appliances/equipment. In the case of peer-to-peer medical teachings, medical device companies fly in surgeons from all over the world to attend live surgeries.</p>
  </div>
</section>

<section class="benefits">
  <div class="panel">
    <h2>Benefits</h2>
    <p class="sub">simply dummy text of the printing and type-setting industry.</p>
    <div class="tab active" style="top:182px">More effective learning</div>
    <div class="tab" style="top:244px">Faster sharing &amp; tecniques</div>
    <div class="tab" style="top:306px">More cost effective</div>
  </div>
  <div class="video">
    <div class="frame" role="img" aria-label="Video still of surgeons working beside a monitor in an operating room">
      <div class="play"><svg width="30" height="34" viewBox="0 0 36 40"><path d="M6 2l28 18L6 38z" fill="#fff"/></svg></div>
    </div>
  </div>
</section>

<section class="products">
  <h2 class="section-title">Our Products</h2>
  <div class="product-row">
    <div class="product"><div class="shot" role="img" aria-label="Live hardware expansion card"></div><h3>Live</h3><p>Almost daily medical device companies, doctors and surgeons all over the world surgical techniques.</p><a class="more" href="#">+ more info</a></div>
    <div class="product"><div class="shot" role="img" aria-label="bTamo control console"></div><h3>o bTamo</h3><p>Almost daily medical device companies, doctors and surgeons all over the world surgical techniques.</p><a class="more" href="#">+ more info</a></div>
    <div class="product"><div class="shot" role="img" aria-label="bTamo local expansion card"></div><h3>o bTamo local</h3><p>Almost daily medical device companies, doctors and surgeons all over the world surgical techniques.</p><a class="more" href="#">+ more info</a></div>
    <div class="product"><div class="shot" role="img" aria-label="bTamo cloud control console with lit faders"></div><h3>o bTamo cloud</h3><p>Almost daily medical device companies, doctors and surgeons all over the world surgical techniques.</p><a class="more" href="#">+ more info</a></div>
  </div>
</section>

<section class="solutions">
  <h2 class="section-title">Solution</h2>
  <div class="card" style="left:80px">
    <div class="img" role="img" aria-label="Team gathered around a table reviewing documents" style="background:linear-gradient(135deg,#c8a47a,#6f7f8e 60%,#3f4c5a)"></div>
    <h3>For Medical Device</h3>
    <p>Almost daily medical device companies, doctors and surgeons all over the world develop new or breakthrough products, medical and surgical techniques. These techniques save lives or increase the survival rate of some patients.</p>
    <a class="btn hot" href="#">Read More</a>
  </div>
  <div class="card" style="left:436px">
    <div class="img" role="img" aria-label="Doctors in white coats in discussion at a meeting" style="background:linear-gradient(135deg,#dfe8ee,#8fb0c8 55%,#4d6f8a)"></div>
    <h3>Doctor &amp; surgeons</h3>
    <p>Almost daily medical device companies, doctors and surgeons all over the world develop new or breakthrough products, medical and surgical techniques. These techniques save lives or increase the survival.</p>
    <a class="btn" href="#">Read More</a>
  </div>
  <div class="card" style="left:792px">
    <div class="img" role="img" aria-label="Person working on a laptop at a desk" style="background:linear-gradient(135deg,#2c2c30,#6b6e78 50%,#e4e6ea)"></div>
    <h3>Medical Conferences</h3>
    <p>Almost daily medical device companies, doctors and surgeons all over the world develop new or breakthrough products, medical and surgical techniques.</p>
    <a class="btn" href="#">Read More</a>
  </div>
</section>

<footer class="footer">
  <div class="brand"><span class="dot"></span>Quorvia</div>
  <div class="links">
    <a href="#">HOME</a><i>|</i><a href="#">ABOUT US</a><i>|</i><a href="#">FEATURES</a><i>|</i><a href="#">BENEFITS</a><i>|</i><a href="#">REFERENCES</a><i>|</i><a href="#">PRODUCTS</a><i>|</i><a href="#">SOLUTIONS</a><i>|</i><a href="#">CONTACT</a>
  </div>
  <p class="copy">Copyright © 2016.Quorvia Deffered live Medical . All rights reserved</p>
  <div class="diamonds"><span></span><span></span><span></span><span></span></div>
</footer>

</body>
</html>
```